marketing card

I need a fun and striking Marketing card to introduce our new office to attract new patients
our website is smilepathwaykids@mailbrook.net for more ideas
add coupon for $25.00 off your next filling
add coupon for free teeth whitening
make the card 9x6 size ,
The card downloaded I like rediscover your smile
free teeth whitening after exam,x-rays & cleaning
Target Market(s)
population in our area , anyone looking for a dental office
Industry/Entity Type
Health Care
Font styles to use
Serif
Colors
33a6d7
9bcb3c
Requirements
Must have
- Coupon for $25 off if you need a filling
- free whitening after teeth cleaning, x-rays & exam
- Our hygienist will come to you if you are home bound or in a nursing home facility
Nice to have
- want to be inviting and non intimating, we see all ages

```html
<!DOCTYPE html>
<html lang="en">
<head>
<meta charset="utf-8">
<title>Smile Pathway – Welcome to Our New Office</title>
<link rel="stylesheet" href="https://fonts.googleapis.com/css2?family=Playfair+Display:ital,wght@1,400;1,700&family=Roboto+Condensed:wght@400;700&display=swap">
<style>
  :root {
    --brand-blue: #33a6d7;
    --brand-green: #9bcb3c;
    --sky-light: #ffffff;
    --sky-mid: #cfe9f5;
    --sky-deep: #6fbbe0;
    --ink: #111111;
    --white: #ffffff;
    --logo-panel: #cfe0f2;
    --logo-ink: #1f3d6b;
    --photo-top: #dbe7ee;
    --photo-bottom: #8fa3bd;
  }
  * { margin: 0; padding: 0; box-sizing: border-box; }
  html, body { width: 1200px; height: 800px; overflow: hidden; background: var(--white); }
  .card {
    position: relative;
    width: 1200px;
    height: 800px;
    overflow: hidden;
    background: linear-gradient(180deg, var(--sky-light) 0%, var(--sky-light) 30%, var(--sky-mid) 55%, var(--sky-deep) 100%);
    font-family: "Roboto Condensed", "Arial Narrow", sans-serif;
    color: var(--ink);
  }
  .headline-banner {
    position: absolute;
    left: 57px; top: 17px;
    width: 1073px; height: 187px;
    background: var(--brand-blue);
    border: 5px solid var(--white);
    outline: 1px solid #d5dde2;
    box-shadow: 0 10px 10px -6px rgba(0,0,0,0.55);
    z-index: 3;
  }
  .headline-banner span {
    position: absolute;
    font-family: "Playfair Display", Georgia, serif;
    font-style: italic;
    color: var(--white);
    line-height: 1;
    white-space: nowrap;
  }
  .headline-welcome { left: 40px; top: 14px; font-size: 70px; }
  .headline-office { left: 300px; top: 82px; font-size: 100px; }

  .tagline {
    position: absolute;
    left: 70px; top: 216px;
    font-family: "Playfair Display", Georgia, serif;
    font-style: italic;
    font-size: 39px;
    line-height: 1;
    white-space: nowrap;
    z-index: 3;
  }
  .promise {
    position: absolute;
    right: 60px; top: 268px;
    font-family: "Playfair Display", Georgia, serif;
    font-style: italic;
    font-size: 51px;
    line-height: 1;
    white-space: nowrap;
    z-index: 3;
  }
  .promise .accent { color: var(--brand-blue); font-weight: 700; }

  .family-photo {
    position: absolute;
    left: 20px; top: 322px;
    width: 600px; height: 383px;
    background: linear-gradient(180deg, var(--photo-top) 0%, var(--photo-bottom) 100%);
    border-radius: 120px 120px 0 0;
    z-index: 1;
  }

  .offers {
    position: absolute;
    left: 621px; top: 334px;
    width: 545px; height: 245px;
    background: var(--brand-green);
    border: 5px solid var(--white);
    box-shadow: 0 4px 10px rgba(0,0,0,0.25);
    z-index: 2;
  }
  .offers .divider {
    position: absolute;
    left: 251px; top: 17px;
    width: 4px; height: 202px;
    background: var(--white);
  }
  .offer {
    position: absolute;
    top: 0;
    text-align: center;
    line-height: 1;
  }
  .offer-whitening { left: 0; width: 251px; }
  .offer-filling { left: 255px; width: 285px; }
  .offer-title { display: block; font-weight: 700; font-size: 64px; margin-top: 40px; }
  .offer-line { display: block; font-size: 32px; margin-top: 10px; }
  .offer-fine { display: block; font-weight: 700; font-size: 17px; margin-top: 8px; }
  .offer-fine + .offer-fine { margin-top: 4px; }
  .offer-filling .offer-line + .offer-line { margin-top: 12px; }

  .brand-panel {
    position: absolute;
    left: 739px; top: 593px;
    width: 307px; height: 129px;
    background: var(--logo-panel);
    border: 3px solid var(--white);
    display: flex;
    align-items: center;
    justify-content: center;
    z-index: 4;
  }
  .brand-name {
    font-family: "Roboto Condensed", "Arial Narrow", sans-serif;
    font-weight: 700;
    font-size: 46px;
    color: var(--logo-ink);
    white-space: nowrap;
  }

  .contact-band {
    position: absolute;
    left: 0; top: 705px;
    width: 1200px; height: 95px;
    background: var(--brand-green);
    z-index: 3;
  }
  .call-label {
    position: absolute;
    left: 45px; top: 28px;
    font-size: 28px;
    line-height: 1;
  }
  .call-number {
    position: absolute;
    left: 157px; top: 12px;
    font-size: 52px;
    font-weight: 700;
    line-height: 1;
  }
  .web-address {
    position: absolute;
    left: 671px; top: 24px;
    font-size: 37px;
    line-height: 1;
  }
  .home-visit {
    position: absolute;
    left: 0; top: 70px;
    width: 1200px;
    text-align: center;
    font-size: 18px;
    font-weight: 700;
    line-height: 1;
  }
</style>
</head>
<body>
<div class="card">
  <header class="headline-banner">
    <span class="headline-welcome">Welcome to</span>
    <span class="headline-office">Our New Office</span>
  </header>

  <p class="tagline">We are here for what's best for you, not what best for us!</p>
  <p class="promise"><span class="accent">YOU</span> deserve <span class="accent">Excellent Dental Care</span>.</p>

  <div class="family-photo" role="img" aria-label="Photo of a smiling family: a father carrying his son piggyback and a mother hugging her daughter"></div>

  <section class="offers">
    <div class="offer offer-whitening">
      <span class="offer-title">Free</span>
      <span class="offer-line">Teeth Whitening</span>
      <span class="offer-fine">after teeth cleaning,</span>
      <span class="offer-fine">x-rays &amp; examination</span>
    </div>
    <div class="divider"></div>
    <div class="offer offer-filling">
      <span class="offer-title">$25 off</span>
      <span class="offer-line">in your next filling</span>
      <span class="offer-line">if you need a filling</span>
    </div>
  </section>

  <div class="brand-panel">
    <span class="brand-name">Smile Pathway</span>
  </div>

  <footer class="contact-band">
    <span class="call-label">Call Us:</span>
    <span class="call-number">385-555-0142</span>
    <span class="web-address">www.smilepathwaykids.com</span>
    <span class="home-visit">Home bound or in a nursing home? Our hygienist will come to you!</span>
  </footer>
</div>
</body>
</html>
```